New company aimed at high net worth individuals needs a stationery design

We need a stationery design for a new company that is offering High Net Worth Individuals around the world a Tailored Benevolence service (enabling them to realise their personal aspirations in 'tailored benevolence'). Not looking for a logo because we think 'Tailored Benevolence...' speaks for itself. Looking for a clean look that smacks of (understated) quality and reliability to the billionaires who open our letters and folders.

Target Market(s)

High Net Worth Individuals, millionaires, CEOs of Companies, stock brokers, asset managers. Extremely wealthy individuals.

Industry/Entity Type

It Company

Contact Information for Business Card

Dr Gerald Finchley. Tailored Benevolence...
17 Corlett Crescent, Shipston on Stour, Warwickshire, CV31 9PT.
gerald.finchley@tailoredbenevolex.co.uk
www.tailoredbenevolex.co.uk
In UK: 07983 604527
Global: +44 7983 604527

Font styles to use
Serif
Decorative

Requirements
Must have
• clean look (I used to like the Global Treasury Business cards!). understated air of high quality. however I think that I like 'Tailored Benevolence...' rather than 'Tailored Benevolence Ltd.' because the former hints (I think at least) that you are on a journey leading to somewhere that can be great. whole aim of company is to get inside the clients hearts and enable them to achieve their personal dreams of helping people. Wife thinks a thumbprint or handprint somewhere might be good (I know what she means but I am not convinced)
Nice to have
• I would like the stationery to bear the words 'Tailored Benevolence...' the three dots signify that this is going to lead somewhere, something is going to happen. I am thinking about a strapline for the letterhead and folder: your experience - your heart - your legacy.
Should not have
• must not look like a business card from a charity or NGO.

```html
<!DOCTYPE html>
<html lang="en">
<head>
<meta charset="utf-8">
<title>Tailored Benevolence – Business Card</title>
<link rel="stylesheet" href="https://fonts.googleapis.com/css2?family=Tinos:wght@700&family=Questrial&display=swap">
<style>
  :root {
    --backdrop: #e8e9eb;
    --card-white: #fbfbfb;
    --card-black: #222222;
    --ink: #151515;
    --ink-soft: #333333;
    --ink-reverse: #e6e6e6;
    --shadow: rgba(0, 0, 0, 0.14);
  }
  * { box-sizing: border-box; margin: 0; padding: 0; }
  html, body {
    width: 1200px;
    height: 1000px;
    overflow: hidden;
    background: var(--backdrop);
  }
  .stage {
    position: relative;
    width: 1200px;
    height: 1000px;
  }
  .card {
    position: absolute;
    top: 357px;
    width: 500px;
    height: 286px;
    box-shadow: 0 10px 28px var(--shadow);
  }
  .card-front {
    left: 70px;
    background: var(--card-white);
    color: var(--ink);
  }
  .card-back {
    left: 630px;
    background: var(--card-black);
    display: flex;
    align-items: center;
    justify-content: center;
  }
  .brand {
    font-family: "Tinos", "Times New Roman", serif;
    font-weight: 700;
    letter-spacing: 0.2px;
  }
  .card-front .brand {
    position: absolute;
    top: 42px;
    right: 40px;
    font-size: 24px;
    color: var(--ink);
  }
  .card-back .brand {
    font-size: 30px;
    color: var(--ink-reverse);
  }
  .holder {
    position: absolute;
    top: 100px;
    left: 40px;
    font-family: "Questrial", "Century Gothic", sans-serif;
  }
  .holder-name {
    font-size: 14px;
    font-weight: 700;
    letter-spacing: 0.6px;
    -webkit-text-stroke: 0.4px var(--ink);
  }
  .holder-role {
    font-size: 11.5px;
    color: var(--ink-soft);
    margin-top: 2px;
  }
  .contact {
    position: absolute;
    left: 40px;
    bottom: 44px;
    font-family: "Questrial", "Century Gothic", sans-serif;
    font-size: 11px;
    line-height: 1.6;
    color: var(--ink-soft);
  }
  .contact b {
    color: var(--ink);
    font-weight: 700;
  }
</style>
</head>
<body>
  <main class="stage">
    <section class="card card-front" aria-label="Business card front">
      <p class="brand">Tailored Benevolence</p>
      <div class="holder">
        <p class="holder-name">MARCUS ELLWOOD</p>
        <p class="holder-role">General Manager</p>
      </div>
      <div class="contact">
        <p>42 Harrowgate Lane : 3rd Floor, Kestrel Bay, KB 20417</p>
        <p><b>T:</b> 415-730-5186 · <b>E:</b> marcus@ellwoodmail.com · <b>W:</b> www.ellwoodmail.com</p>
      </div>
    </section>
    <section class="card card-back" aria-label="Business card back">
      <p class="brand">Tailored Benevolence</p>
    </section>
  </main>
</body>
</html>
```